Visitenkarten-Design für Fachärztin für Allgemeinmedizin
Zielgruppe
Visitenkarte passend zum Logo mit folgenden Daten:
Dr. med Miriam Valdorf
Fachärztin für Allgemeinmedizin
Brennwaldweg 14
72946 Steinhofen OT Talgrund
Telefon 07451/8194
Website: www.hausarztpraxis-talgrund.de
Online Terminvereinbarung
Sprechstunde
Mo 8-11:30Uhr sowie 14-17 Uhr
Die 8-13 Uhr
Mi 8-13 Uhr
Do 8-11:30uhr sowie 14-18 Uhr
Fr 8- 11:30Uhr
Sowie nach Vereinbarung
Laborzeiten tägl. 7:15 -8 Uhr
Telefonzeiten tägl. 8-11 Uhr , sowie Mo und Fr 14-16 Uhr
Aufgabenstellung
Nach dem Logo, welches hier erstellt wurde Visitenkarten ..
vorher und Rückseite!
Sprechzeiten, Name, Adresse , Tele Fax und Website
In den Farben des Magenta und Grau

```html
<!DOCTYPE html>
<html lang="de">
<head>
<meta charset="utf-8">
<title>Visitenkarte Hausarztpraxis Dr. med. Miriam Valdorf</title>
<link rel="stylesheet" href="https://fonts.googleapis.com/css2?family=Cormorant+SC:wght@600;700&family=Open+Sans:wght@400;600;700&display=swap">
<style>
  :root {
    --magenta: #c41a5c;
    --grey: #5a5e63;
    --grey-light: #e4e4e6;
    --white: #ffffff;
    --stage: #2b2b2d;
    --serif: "Cormorant SC", "Times New Roman", serif;
    --sans: "Open Sans", Arial, sans-serif;
  }
  * { box-sizing: border-box; margin: 0; padding: 0; }
  html, body { width: 1200px; height: 900px; overflow: hidden; }
  body {
    background: var(--stage);
    font-family: var(--sans);
    display: flex; align-items: center; justify-content: center; gap: 50px;
  }
  .card {
    position: relative; width: 520px; height: 310px;
    background: var(--white); overflow: hidden;
    box-shadow: 0 10px 30px rgba(0,0,0,.5);
  }

  /* Vorderseite: Sprechzeiten */
  .front-head {
    height: 118px; display: flex; flex-direction: column; align-items: center; justify-content: center;
    border-bottom: 3px solid var(--grey);
  }
  .brand-mark {
    width: 40px; height: 40px; border-radius: 50%;
    border: 4px solid var(--magenta); margin-bottom: 4px;
  }
  .brand-kicker { font-family: var(--serif); font-size: 13px; letter-spacing: 3px; color: var(--grey); font-weight: 600; }
  .brand-name {
    font-family: var(--serif); font-size: 20px; font-weight: 700; color: var(--magenta);
    border-top: 1px solid var(--grey); border-bottom: 1px solid var(--grey); padding: 0 8px; line-height: 1.2;
  }
  .brand-tagline { font-family: var(--serif); font-size: 9px; letter-spacing: 1.5px; color: var(--grey); margin-top: 2px; }
  .front-band {
    position: absolute; left: 0; right: 0; top: 124px; bottom: 0; background: var(--magenta);
    color: var(--white); display: flex; padding: 26px 34px; gap: 30px;
  }
  .deco-ring {
    position: absolute; right: 40px; top: 20px; width: 150px; height: 150px; border-radius: 50%;
    border: 14px solid rgba(255,255,255,.12);
  }
  .hours { flex: 1; font-size: 12.5px; line-height: 1.45; position: relative; }
  .hours h3 { font-size: 12.5px; font-weight: 700; text-transform: uppercase; }
  .hours .note { margin-top: 14px; font-weight: 700; text-transform: uppercase; letter-spacing: 1px; }
  .reach { flex: 1; font-size: 12px; font-weight: 700; text-transform: uppercase; line-height: 1.45; position: relative; }
  .reach p + p { margin-top: 30px; }

  /* Rückseite: Kontakt */
  .back-deco {
    position: absolute; left: 30px; top: 40px; width: 230px; height: 230px; border-radius: 50%;
    border: 16px solid var(--grey-light);
  }
  .back-brand { position: absolute; left: 50px; top: 62px; width: 190px; text-align: center; }
  .back-brand .kicker { font-family: var(--serif); font-size: 22px; font-weight: 700; color: var(--magenta); }
  .back-brand .brand-mark { width: 96px; height: 96px; border-width: 8px; margin: 14px auto 0; }
  .contact { position: absolute; left: 285px; top: 40px; width: 215px; color: var(--grey); font-size: 12.5px; }
  .contact .name { font-family: var(--serif); font-size: 17px; font-weight: 700; color: var(--magenta); line-height: 1.1; }
  .contact .title { font-size: 10.5px; padding-bottom: 6px; border-bottom: 2px solid var(--magenta); }
  .contact .address { margin-top: 12px; line-height: 1.35; }
  .contact .hotline { margin-top: 10px; font-size: 9.5px; font-weight: 700; color: var(--magenta); text-transform: uppercase; }
  .contact .line { display: flex; align-items: center; gap: 6px; line-height: 1.4; }
  .contact svg { width: 11px; height: 11px; fill: var(--magenta); }
  .web-strip {
    position: absolute; left: 0; right: 0; top: 212px; height: 22px; background: var(--magenta);
    color: var(--white); font-size: 11.5px; font-weight: 700; text-align: right; padding: 3px 20px;
  }
  .booking-strip {
    position: absolute; left: 0; right: 0; bottom: 0; height: 34px; background: var(--magenta);
    color: var(--white); font-size: 14px; padding: 7px 22px;
  }
</style>
</head>
<body>

<section class="card card-front">
  <header class="front-head">
    <div class="brand-mark"></div>
    <div class="brand-kicker">HAUSARZTPRAXIS</div>
    <div class="brand-name">Dr. med. Miriam Valdorf</div>
    <div class="brand-tagline">MIT HERZ UND SORGFALT FÜR SIE DA</div>
  </header>
  <div class="front-band">
    <div class="deco-ring"></div>
    <div class="hours">
      <h3>Sprechstunde</h3>
      <p>Mo 8-12:00 Uhr sowie 15-18 Uhr</p>
      <p>Di 7-12 Uhr</p>
      <p>Mi 9-12 Uhr</p>
      <p>Do 8-12:00 Uhr sowie 15-19 Uhr</p>
      <p>Fr 7- 12:00 Uhr</p>
      <p class="note">Sowie nach Vereinbarung</p>
    </div>
    <div class="reach">
      <p>Laborzeiten tägl. 7:30 -8:30 Uhr</p>
      <p>Telefonische Erreichbarkeit<br>tägl. 8-12 Uhr,<br>sowie Di und Do 15-17 Uhr</p>
    </div>
  </div>
</section>

<section class="card card-back">
  <div class="back-deco"></div>
  <div class="back-brand">
    <div class="kicker">HAUSARZTPRAXIS</div>
    <div class="brand-mark"></div>
  </div>
  <div class="contact">
    <div class="name">Dr. med. Miriam Valdorf</div>
    <div class="title">Fachärztin für Allgemeinmedizin</div>
    <div class="address">Brennwaldweg 14<br>72946 Steinhofen OT Talgrund</div>
    <div class="hotline">Terminvereinbarung &amp; Rezepthotline</div>
    <div class="line">
      <svg viewBox="0 0 24 24"><path d="M6.6 10.8a15.1 15.1 0 0 0 6.6 6.6l2.2-2.2c.3-.3.7-.4 1-.2 1.1.4 2.3.6 3.6.6.6 0 1 .4 1 1V20c0 .6-.4 1-1 1A17 17 0 0 1 3 4c0-.6.4-1 1-1h3.5c.6 0 1 .4 1 1 0 1.3.2 2.5.6 3.6.1.3 0 .7-.2 1z"/></svg>
      <span>07451/8194</span>
    </div>
    <div class="line">
      <svg viewBox="0 0 24 24"><path d="M6 2h9l3 3v5H6z M3 11h18v9h-3v2H6v-2H3z"/></svg>
      <span>07451-81957</span>
    </div>
  </div>
  <div class="web-strip">www.hausarztpraxis-talgrund.de</div>
  <div class="booking-strip">Online Terminvereinbarung</div>
</section>

</body>
</html>
```